law firm seeking modern professional FB design

We have an existing FB page and wish to have a professional design for it (see FB Marrow Legal). We also have a web site and business cards with a basic logo and want this logo improved or replaced.

We would like the FB page to be eye catching and stand out. The page features advertisements and articles of general interest and we want a design that fits in with the material that is presented.

The business is seeking to attract reasonably affluent clients seeking legal advice and representation in family law matters.

Target Market(s)

legal services offered in family law - target market being people in relationships that have ended for property and parenting disputes/advice.

Industry/Entity Type

Legal

Contact Information for Business Card

see attachment provided for proposed general lay out with logot o be replaced..

Font styles to use
Sans Serif

Colors
0355a3
a54499
b7b7b7
000000
ec1f27
ffc214

Requirements
Must have
• Modern professional looking FB page and logo that fits in with current website design at marrow.legal
Nice to have
• Have open mind about what will work
• *For the business card design it also needs to incorporate a second logo (already designed) that is in teh upload section below.

```html
<!DOCTYPE html>
<html lang="en">
<head>
<meta charset="utf-8">
<title>Marrow Legal – Cover</title>
<link href="https://fonts.googleapis.com/css2?family=Roboto:wght@300;400;500&display=swap" rel="stylesheet">
<style>
  :root {
    --panel: #4a4a4a;
    --white: #ffffff;
    --text-soft: #e6e6e6;
    --icon-dark: #4a4a4a;
    --brand-blue: #0355a3;
    --brand-purple: #a54499;
    --brand-grey: #b7b7b7;
    --brand-black: #000000;
    --brand-red: #ec1f27;
    --brand-yellow: #ffc214;
    --glass-light: #e3e9ec;
    --glass-mid: #b8c2c8;
    --suit-dark: #2a2d31;
    --floor: #cfd5d8;
  }
  html, body {
    margin: 0;
    padding: 0;
    overflow: hidden;
    background: var(--white);
  }
  .cover {
    position: relative;
    width: 1200px;
    height: 444px;
    overflow: hidden;
    font-family: "Roboto", Arial, sans-serif;
    color: var(--white);
  }
  .team-photo {
    position: absolute;
    inset: 0 400px 0 0;
    background:
      linear-gradient(180deg, transparent 0%, transparent 30%, rgba(42,45,49,0.55) 42%, rgba(42,45,49,0.75) 60%, rgba(42,45,49,0.35) 78%, transparent 88%),
      linear-gradient(90deg, rgba(3,85,163,0.18) 0%, rgba(3,85,163,0.04) 40%, rgba(3,85,163,0.14) 75%, rgba(3,85,163,0.22) 100%),
      linear-gradient(180deg, var(--glass-light) 0%, var(--glass-mid) 55%, var(--floor) 100%);
  }
  .info-panel {
    position: absolute;
    inset: 0;
    background: var(--panel);
    clip-path: polygon(663px 0, 1200px 0, 1200px 444px, 557px 444px);
  }
  .brand {
    position: absolute;
    left: 932px;
    top: 82px;
    transform: translateX(-50%);
    text-align: center;
    white-space: nowrap;
  }
  .brand-mark {
    display: block;
    width: 14px;
    height: 14px;
    margin: 0 auto 12px;
    border-radius: 50%;
    background: var(--white);
  }
  .brand-name {
    margin: 0;
    font-size: 29px;
    font-weight: 400;
    letter-spacing: 2.5px;
    line-height: 1;
  }
  .brand-tagline {
    margin: 6px 0 0;
    font-size: 10px;
    font-weight: 400;
    color: var(--text-soft);
  }
  .social {
    position: absolute;
    top: 204px;
    left: 866px;
    display: flex;
    gap: 14px;
  }
  .social span {
    width: 18px;
    height: 18px;
    border-radius: 50%;
  }
  .social .s1 { background: var(--brand-blue); }
  .social .s2 { background: var(--brand-purple); }
  .social .s3 { background: var(--brand-grey); }
  .social .s4 { background: var(--brand-red); }
  .social .s5 { background: var(--brand-yellow); }
  .values {
    position: absolute;
    top: 277px;
    left: 0;
    width: 1200px;
    height: 100px;
  }
  .value {
    position: absolute;
    width: 120px;
    transform: translateX(-50%);
    text-align: center;
  }
  .value svg { display: block; margin: 0 auto; }
  .value-label {
    margin-top: 12px;
    font-size: 14px;
    font-weight: 400;
  }
  .contact {
    position: absolute;
    top: 394px;
    left: 0;
    width: 1200px;
    font-size: 12px;
    font-weight: 500;
  }
  .contact-item {
    position: absolute;
    display: flex;
    align-items: center;
    gap: 10px;
    white-space: nowrap;
  }
</style>
</head>
<body>
<div class="cover">
  <div class="team-photo" role="img" aria-label="Photograph of a group of business professionals walking through a bright glass office lobby"></div>
  <div class="info-panel"></div>

  <div class="brand">
    <span class="brand-mark"></span>
    <h1 class="brand-name">MARROW LEGAL</h1>
    <p class="brand-tagline">Representative in family matters</p>
  </div>

  <div class="social" aria-label="Social profiles">
    <span class="s1"></span><span class="s2"></span><span class="s3"></span><span class="s4"></span><span class="s5"></span>
  </div>

  <div class="values">
    <div class="value" style="left:747px">
      <svg width="60" height="60" viewBox="0 0 60 60" aria-hidden="true">
        <circle cx="30" cy="30" r="30" fill="var(--white)"/>
        <path d="M18 28a12 12 0 0 1 21-7" fill="none" stroke="var(--icon-dark)" stroke-width="4"/>
        <path d="M42 15v9h-9z" fill="var(--icon-dark)"/>
        <path d="M42 32a12 12 0 0 1-21 7" fill="none" stroke="var(--icon-dark)" stroke-width="4"/>
        <path d="M18 45v-9h9z" fill="var(--icon-dark)"/>
      </svg>
      <div class="value-label">Our Value #1</div>
    </div>
    <div class="value" style="left:866px">
      <svg width="60" height="60" viewBox="0 0 60 60" aria-hidden="true">
        <circle cx="30" cy="30" r="30" fill="var(--white)"/>
        <rect x="17" y="26" width="5" height="15" fill="var(--icon-dark)"/>
        <rect x="24" y="18" width="5" height="23" fill="var(--icon-dark)"/>
        <rect x="31" y="22" width="5" height="19" fill="var(--icon-dark)"/>
        <rect x="38" y="29" width="5" height="12" fill="var(--icon-dark)"/>
        <rect x="15" y="42" width="30" height="2" fill="var(--icon-dark)"/>
      </svg>
      <div class="value-label">Our Value #2</div>
    </div>
    <div class="value" style="left:991px">
      <svg width="60" height="60" viewBox="0 0 60 60" aria-hidden="true">
        <circle cx="30" cy="30" r="30" fill="var(--white)"/>
        <path d="M30 13a10 10 0 0 0-6 18v5h12v-5a10 10 0 0 0-6-18z" fill="var(--icon-dark)"/>
        <rect x="25" y="38" width="10" height="3" fill="var(--icon-dark)"/>
        <rect x="26" y="43" width="8" height="3" rx="1.5" fill="var(--icon-dark)"/>
      </svg>
      <div class="value-label">Our Value #3</div>
    </div>
    <div class="value" style="left:1124px">
      <svg width="60" height="60" viewBox="0 0 60 60" aria-hidden="true">
        <circle cx="30" cy="30" r="30" fill="var(--white)"/>
        <path d="M30 14l4.7 10 10.8 1.2-8 7.4 2.2 10.7L30 37.9l-9.7 5.4 2.2-10.7-8-7.4 10.8-1.2z" fill="var(--icon-dark)"/>
      </svg>
      <div class="value-label">Our Value #4</div>
    </div>
  </div>

  <div class="contact">
    <div class="contact-item" style="left:636px">
      <svg width="12" height="16" viewBox="0 0 12 16" aria-hidden="true">
        <path d="M6 0a6 6 0 0 0-6 6c0 4.5 6 10 6 10s6-5.5 6-10a6 6 0 0 0-6-6zm0 8.5A2.5 2.5 0 1 1 6 3.5a2.5 2.5 0 0 1 0 5z" fill="var(--white)"/>
      </svg>
      <span>24 Elm Row, London</span>
    </div>
    <div class="contact-item" style="left:815px">
      <svg width="15" height="11" viewBox="0 0 15 11" aria-hidden="true">
        <rect width="15" height="11" fill="var(--white)"/>
        <path d="M0 0l7.5 6L15 0" fill="none" stroke="var(--panel)" stroke-width="1.4"/>
      </svg>
      <span>hello@marrow.legal</span>
    </div>
    <div class="contact-item" style="left:988px">
      <svg width="14" height="14" viewBox="0 0 14 14" aria-hidden="true">
        <path d="M3 0l2.5 3.5-1.5 2a8 8 0 0 0 4.5 4.5l2-1.5L14 11l-1.5 2.5C6 14 0 8 .5 1.5z" fill="var(--white)"/>
      </svg>
      <span>0201555014 - 0203555019</span>
    </div>
  </div>
</div>
</body>
</html>
```